Brightfield Chiropractic Business Cards

Business cards with new logo design. Will upload copy of current card. We like the layout, but we need a new logo. Family, husband holding up baby toward sky, mom and other child standing next to him. We will probably want to include a catch phrase with logo. TBD

```html
<!DOCTYPE html>
<html lang="en">
<head>
<meta charset="utf-8">
<title>Brightfield Chiropractic – Identity &amp; Business Cards</title>
<link href="https://fonts.googleapis.com/css2?family=Montserrat:wght@400;600&display=swap" rel="stylesheet">
<style>
  :root {
    --orange: #f58220;
    --charcoal: #404040;
    --ink: #3d3d3d;
    --tag-grey: #555555;
    --paper: #ffffff;
    --map-fill: #f1f1f1;
    --muted-light: #cfcfcf;
  }
  * { margin: 0; padding: 0; box-sizing: border-box; }
  html, body { width: 1200px; height: 960px; overflow: hidden; background: var(--paper); }
  body { position: relative; font-family: "Montserrat", sans-serif; color: var(--ink); }

  .logo { position: absolute; text-align: center; }
  .logo-mark { display: block; margin: 0 auto; border-radius: 50%; background: var(--orange); }
  .logo-name { font-weight: 600; white-space: nowrap; text-transform: uppercase; line-height: 1.05; }
  .logo-tagline { font-weight: 400; letter-spacing: 0.22em; text-transform: uppercase; white-space: nowrap; }

  .logo--horizontal { left: 40px; top: 250px; width: 490px; }
  .logo--horizontal .logo-mark { width: 90px; height: 90px; margin-bottom: 36px; }
  .logo--horizontal .logo-name { font-size: 33px; color: var(--ink); }
  .logo--horizontal .logo-tagline { font-size: 12px; color: var(--tag-grey); margin-top: 12px; }

  .logo--stacked { left: 130px; top: 560px; width: 320px; }
  .logo--stacked .logo-mark { width: 90px; height: 90px; margin-bottom: 30px; }
  .logo--stacked .logo-name { font-size: 36px; color: var(--ink); }
  .logo--stacked .logo-tagline { font-size: 12px; color: var(--tag-grey); margin-top: 8px; }

  .card { position: absolute; border-radius: 24px; overflow: hidden; }
  .card--front { left: 562px; top: 78px; width: 300px; height: 540px; background: var(--charcoal); color: var(--paper); text-align: center; }
  .card--front .logo { left: 0; top: 110px; width: 300px; }
  .card--front .logo-mark { width: 80px; height: 80px; margin-bottom: 24px; }
  .card--front .logo-name { font-size: 30px; color: var(--paper); }
  .card--front .logo-tagline { font-size: 10.5px; color: var(--muted-light); margin-top: 6px; letter-spacing: 0.2em; }

  .contact { position: absolute; left: 0; top: 358px; width: 300px; }
  .contact-name { font-size: 21px; font-weight: 600; color: var(--orange); text-transform: uppercase; }
  .contact-title { font-size: 15px; text-transform: uppercase; margin-top: 2px; letter-spacing: 0.02em; }
  .contact-lines { margin-top: 20px; font-size: 17px; line-height: 1.38; }

  .card--back { left: 850px; top: 348px; width: 308px; height: 553px; background: var(--orange); color: var(--paper); text-align: center; }
  .location-map { position: absolute; left: 21px; top: 23px; width: 266px; height: 265px; border-radius: 28px; background: var(--map-fill); }
  .address { position: absolute; left: 0; top: 304px; width: 308px; font-size: 19px; line-height: 1.38; }
  .card--back .logo { left: 0; top: 445px; width: 308px; }
  .card--back .logo-mark { width: 36px; height: 36px; margin-bottom: 8px; }
  .card--back .logo-name { font-size: 13px; color: var(--ink); }
  .card--back .logo-tagline { font-size: 5px; color: var(--ink); margin-top: 2px; letter-spacing: 0.15em; }
</style>
</head>
<body>

  <section class="logo logo--horizontal">
    <span class="logo-mark"></span>
    <p class="logo-name">Brightfield Chiropractic</p>
    <p class="logo-tagline">Lorem ipsum lorem lorem</p>
  </section>

  <section class="logo logo--stacked">
    <span class="logo-mark"></span>
    <p class="logo-name">Brightfield<br>Chiropractic</p>
    <p class="logo-tagline">Lorem ipsum lorem lorem</p>
  </section>

  <article class="card card--front">
    <div class="logo">
      <span class="logo-mark"></span>
      <p class="logo-name">Brightfield<br>Chiropractic</p>
      <p class="logo-tagline">Lorem ipsum lorem lorem</p>
    </div>
    <div class="contact">
      <p class="contact-name">Dr. Daniel Ashford</p>
      <p class="contact-title">Chiropractic Physician</p>
      <p class="contact-lines">503-555-0142<br>www.ashfordchiropractic.com</p>
    </div>
  </article>

  <article class="card card--back">
    <div class="location-map" role="img" aria-label="Street map showing the clinic location between surrounding avenues and roads"></div>
    <p class="address">
      4820 SE Maple Ridge<br>
      Center Dr.<br>
      Maple Ridge, OR 97000<br>
      Phone: (503) 555-0142<br>
      Fax: (503) 555-0187
    </p>
    <div class="logo">
      <span class="logo-mark"></span>
      <p class="logo-name">Brightfield<br>Chiropractic</p>
      <p class="logo-tagline">Lorem ipsum lorem lorem</p>
    </div>
  </article>

</body>
</html>
```